Powerpoint Deign for a sales presentation

I am looking for a powerpoint presentation design with animations of my Bright Horizon Method Blueprint
I would like this to be a path that leads from feeling sad to feeling awesome- due to finding your life purpose (your why)

There are 3 main areas that the client needs to know in order to find their why (purpose) Awareness - Intention & Manifest - these should be designed in grey (as this represents the grey miserable world they stay stuck in if they don't have these skills) and each word will need to be animated to come on one at a time

Each of these has 2 solutions that sits under the required steps
Awareness - The Lantern Insight Process & The Mindful Discovery Builder
Intention - The T.O.N.E Balance Governor & The Marvellous Tomorrow Glow
Manifest - The Vibrant Pathway Mandate & The Thriving Pulse System

& a bonus system called The Spark Plenty Booster - which can be designed to be shown on a separate slide

These "solutions" should be in colour boxes that compliment our branding of red, white & black or even the orange as shown on the examples
I have a version now - but it has been put together over time & look like it doesn't sit together well, and we have added more along the way.
For example the path goes down rather than up (to success)
There is a sad face at the start & then a happy one - it would be better for the happy one to be at the end
The icons are all ok - but the trampoline one can go

Looking for new ideas and revamped ideas

40+ years old (mainly women but not always)

Personal Development

• Merge

F0912C
F2A743
F7CA91
FBE8D2
FDF5EE
EB3D1F
EC4F4E
F09395
F8D3D4
FCEDEE

• animation on the power point

```html
<!DOCTYPE html>
<html lang="en">
<head>
<meta charset="utf-8">
<title>Bright Horizon Method Blueprint</title>
<link href="https://fonts.googleapis.com/css2?family=Didact+Gothic&family=PT+Sans:wght@700&display=swap" rel="stylesheet">
<style>
  :root {
    --bg: #f2f2f2;
    --ink: #111111;
    --red: #e8313a;
    --red-dark: #d92a2f;
    --grey: #a6a6a6;
    --grey-box: #d9d9d9;
    --grey-text: #5a5a5a;
    --orange: #f39a1e;
    --orange-light: #f7ca91;
    --white: #ffffff;
  }
  html, body {
    margin: 0;
    padding: 0;
    width: 1200px;
    height: 675px;
    overflow: hidden;
    background: var(--bg);
  }
  .slide {
    display: block;
    width: 1200px;
    height: 675px;
    background: var(--bg);
  }
  .slide-title {
    font-family: "Didact Gothic", "Century Gothic", sans-serif;
    font-size: 44px;
    letter-spacing: 2.5px;
    fill: var(--ink);
  }
  .stage-label {
    font-family: "Didact Gothic", "Century Gothic", sans-serif;
    font-size: 23px;
    fill: var(--ink);
  }
  .goal-label {
    font-family: "Didact Gothic", "Century Gothic", sans-serif;
    font-size: 22px;
    fill: var(--ink);
  }
  .solution-text {
    font-family: "PT Sans", Arial, sans-serif;
    font-weight: 700;
    font-size: 15px;
  }
  .solution-text.on-red { fill: var(--white); }
  .solution-text.on-grey { fill: var(--grey-text); }
  .brand-name {
    font-family: "Didact Gothic", "Century Gothic", sans-serif;
    font-size: 19px;
    fill: var(--ink);
  }
  .path-red { stroke: var(--red); }
  .path-grey { stroke: var(--grey); }
  .path-orange { stroke: var(--orange); }
  .path-band { fill: none; stroke-width: 18; stroke-linejoin: round; }
  .path-dash { fill: none; stroke: var(--ink); stroke-width: 2; stroke-dasharray: 7 6; }
  .connector { stroke: var(--grey); stroke-width: 2; }
  .icon-line { fill: none; stroke: var(--ink); stroke-width: 2.2; stroke-linecap: round; stroke-linejoin: round; }
  .bulb { fill: var(--white); }
  .bulb-ray { stroke: var(--white); stroke-width: 1.4; stroke-linecap: round; }
</style>
</head>
<body>
<svg class="slide" viewBox="0 0 1280 720" xmlns="http://www.w3.org/2000/svg">
  <!-- Title -->
  <text class="slide-title" x="90" y="96">BRIGHT HORIZON</text>
  <text class="slide-title" x="90" y="152">METHOD</text>
  <text class="slide-title" x="90" y="208">BLUEPRINT</text>

  <!-- Journey path -->
  <g class="journey">
    <path class="path-band path-red" d="M145,605 H283 Q305,605 305,583 V512 Q305,490 327,490 H468 Q490,490 490,468 V402 Q490,380 512,380 H516"/>
    <path class="path-band path-grey" d="M512,380 H638 Q660,380 660,358 V290 Q660,268 682,268 H808"/>
    <path class="path-band path-orange" d="M814,268 Q830,268 830,246 V132 Q830,110 852,110 H990"/>
    <path class="path-dash" d="M145,605 H283 Q305,605 305,583 V512 Q305,490 327,490 H468 Q490,490 490,468 V402 Q490,380 512,380 H638 Q660,380 660,358 V290 Q660,268 682,268 H806"/>
    <path class="path-dash" d="M814,268 Q830,268 830,246 V132 Q830,110 852,110 H990"/>
  </g>

  <!-- Start pin -->
  <g class="pin-start">
    <path d="M148,492 a53,53 0 0 1 37,91 L148,618 L111,583 a53,53 0 0 1 37,-91 z" fill="var(--ink)"/>
    <circle cx="148" cy="545" r="34" fill="var(--red)" role="img" aria-label="Portrait of a sad woman at the start of the path"/>
  </g>

  <!-- End pin -->
  <g class="pin-goal">
    <path d="M1028,64 a53,53 0 0 1 37,91 L1028,188 L991,155 a53,53 0 0 1 37,-91 z" fill="var(--white)" stroke="var(--orange)" stroke-width="1.5"/>
    <circle cx="1028" cy="116" r="36" fill="var(--orange)" role="img" aria-label="Portrait of a happy woman at the end of the path"/>
  </g>
  <text class="goal-label" x="1030" y="216" text-anchor="middle">Thriving</text>
  <text class="goal-label" x="1030" y="245" text-anchor="middle">Pulse</text>
  <text class="goal-label" x="1030" y="274" text-anchor="middle">System</text>

  <!-- Stage: Awareness -->
  <g class="stage stage-awareness">
    <line class="connector" x1="403" y1="490" x2="403" y2="676"/>
    <g class="icon-eye" transform="translate(403,413)">
      <path class="icon-line" d="M-21,0 Q0,-20 21,0 Q0,20 -21,0 z"/>
      <circle class="icon-line" cx="0" cy="0" r="7"/>
      <circle cx="0" cy="0" r="3" fill="var(--ink)"/>
      <path class="icon-line" d="M-12,-13 l-3,-5 M0,-16 v-6 M12,-13 l3,-5"/>
    </g>
    <text class="stage-label" x="401" y="459" text-anchor="middle">Awareness</text>
    <circle cx="403" cy="490" r="21" fill="var(--red-dark)"/>
    <g transform="translate(403,490)">
      <circle class="bulb" cx="0" cy="-2" r="6"/>
      <rect class="bulb" x="-3" y="4" width="6" height="5" rx="1"/>
      <path class="bulb-ray" d="M0,-12 v-2 M-8,-8 l-1.5,-1.5 M8,-8 l1.5,-1.5 M-10,-1 h-2 M10,-1 h2"/>
    </g>
    <rect x="339" y="529" width="128" height="69" fill="var(--red)"/>
    <text class="solution-text on-red" text-anchor="middle" x="403" y="550">The Lantern</text>
    <text class="solution-text on-red" text-anchor="middle" x="403" y="569">Insight</text>
    <text class="solution-text on-red" text-anchor="middle" x="403" y="588">Process</text>
    <rect x="339" y="607" width="128" height="69" fill="var(--red)"/>
    <text class="solution-text on-red" text-anchor="middle" x="403" y="627">The Mindful</text>
    <text class="solution-text on-red" text-anchor="middle" x="403" y="646">Discovery</text>
    <text class="solution-text on-red" text-anchor="middle" x="403" y="665">Builder</text>
  </g>

  <!-- Stage: Intention -->
  <g class="stage stage-intention">
    <line class="connector" x1="582" y1="382" x2="582" y2="563"/>
    <g class="icon-head" transform="translate(578,296)">
      <path class="icon-line" d="M-12,17 V8 Q-20,0 -16,-8 Q-10,-20 4,-18 Q18,-15 18,-2 L22,6 L17,7 V12 Q17,15 12,15 H8 V17"/>
      <path class="icon-line" d="M-2,-6 Q-2,-11 3,-11 Q8,-11 8,-6 Q8,-2 3,0 V3"/>
      <circle cx="3" cy="7" r="1.3" fill="var(--ink)"/>
    </g>
    <text class="stage-label" x="582" y="345" text-anchor="middle">Intention</text>
    <circle cx="582" cy="382" r="21" fill="var(--grey)"/>
    <g transform="translate(582,382)">
      <circle class="bulb" cx="0" cy="-2" r="6"/>
      <rect class="bulb" x="-3" y="4" width="6" height="5" rx="1"/>
      <path class="bulb-ray" d="M0,-12 v-2 M-8,-8 l-1.5,-1.5 M8,-8 l1.5,-1.5 M-10,-1 h-2 M10,-1 h2"/>
    </g>
    <rect x="517" y="417" width="130" height="69" fill="var(--grey-box)"/>
    <text class="solution-text on-grey" text-anchor="middle" x="582" y="437">The T.O.N.E</text>
    <text class="solution-text on-grey" text-anchor="middle" x="582" y="456">Balance</text>
    <text class="solution-text on-grey" text-anchor="middle" x="582" y="475">Governor</text>
    <rect x="517" y="494" width="130" height="69" fill="var(--grey-box)"/>
    <text class="solution-text on-grey" text-anchor="middle" x="582" y="524">The Marvellous</text>
    <text class="solution-text on-grey" text-anchor="middle" x="582" y="543">Tomorrow Glow</text>
  </g>

  <!-- Stage: Manifest -->
  <g class="stage stage-manifest">
    <line class="connector" x1="746" y1="268" x2="746" y2="448"/>
    <g class="icon-team" transform="translate(750,178)">
      <rect class="icon-line" x="-23" y="-24" width="14" height="13"/>
      <rect class="icon-line" x="9" y="-24" width="14" height="13"/>
      <path class="icon-line" d="M-16,-11 V-4 H16 V-11 M0,-4 V2"/>
      <circle class="icon-line" cx="-12" cy="8" r="3.5"/>
      <circle class="icon-line" cx="0" cy="6" r="3.5"/>
      <circle class="icon-line" cx="12" cy="8" r="3.5"/>
      <path class="icon-line" d="M-20,22 Q-20,13 -12,13 Q-6,13 -6,18 M20,22 Q20,13 12,13 Q6,13 6,18 M-7,22 Q-7,11 0,11 Q7,11 7,22"/>
      <path class="icon-line" d="M-24,24 H24"/>
    </g>
    <text class="stage-label" x="747" y="234" text-anchor="middle">Manifest</text>
    <circle cx="746" cy="268" r="21" fill="var(--grey)"/>
    <g transform="translate(746,268)">
      <circle class="bulb" cx="0" cy="-2" r="6"/>
      <rect class="bulb" x="-3" y="4" width="6" height="5" rx="1"/>
      <path class="bulb-ray" d="M0,-12 v-2 M-8,-8 l-1.5,-1.5 M8,-8 l1.5,-1.5 M-10,-1 h-2 M10,-1 h2"/>
    </g>
    <rect x="682" y="302" width="129" height="69" fill="var(--grey-box)"/>
    <text class="solution-text on-grey" text-anchor="middle" x="746" y="322">The Vibrant</text>
    <text class="solution-text on-grey" text-anchor="middle" x="746" y="341">Pathway</text>
    <text class="solution-text on-grey" text-anchor="middle" x="746" y="360">Mandate</text>
    <rect x="682" y="379" width="129" height="69" fill="var(--grey-box)"/>
    <text class="solution-text on-grey" text-anchor="middle" x="746" y="399">The Thriving</text>
    <text class="solution-text on-grey" text-anchor="middle" x="746" y="418">Pulse</text>
    <text class="solution-text on-grey" text-anchor="middle" x="746" y="437">System</text>
  </g>

  <!-- Brand name -->
  <g class="brand">
    <circle cx="1140" cy="648" r="7" fill="var(--red)"/>
    <text class="brand-name" x="1154" y="655">Bright Horizon</text>
  </g>
</svg>
</body>
</html>
```